Design mobile friendly review and ranking site

We're working on a corporate website for reviewing and ranking fellow employees. We need the website to look both fun and professional and it needs to be responsive - to it works on mobile and desktop.

Looking for css and HTML for 3 key pages as well as a header and footer for the site. Also would need any supporting graphics as part of the design.

Target Market(s)

Professionals in their 20s, 30s, and 40s.

Industry/Entity Type

Internet

Coding

Coded - Design and coding required

Number of Pages Required

3 page

Font styles to use
Sans Serif

Requirements
Must have
• 3 key pages we need (note included screenshots for each - these are just super rough cuts so you see examples of the content.)
• a) main-intro: A compelling into page with a login/registration form. Should be sleek/modern/enticing. Also we would show the ranking for the top 3 people to tease people re: content.
• b) main-page: Has two sections: One at the top where you would rate someone and one at the bottom where it shows a ranking of people.
• c) profile page: This is where you view a specific person. You see the person's picture, some info about the person, you see their overall rating, you can rate them, and you also see their historical ratings.
Nice to have
• Note we need css and HTML for this. It should feel as sleek and modern. Note also must be responsive design so it works well in mobile and desktop.

```html
<!DOCTYPE html>
<html lang="en">
<head>
<meta charset="utf-8">
<title>Profile – Sam Rivers</title>
<link href="https://fonts.googleapis.com/css2?family=Open+Sans:wght@400;600&family=Roboto:wght@400&display=swap" rel="stylesheet">
<style>
:root{
  --brand:#3b5499;
  --brand-dark:#253c78;
  --track-dark:#1f3467;
  --page:#f0f1f3;
  --card:#ffffff;
  --line:#dedfe2;
  --text:#333333;
  --muted:#666666;
  --date:#9a9a9a;
  --star-on:#f29a0e;
  --star-off:#555555;
  --avatar:#26a69a;
  --avatar-user:#2c3e63;
}
*{box-sizing:border-box;margin:0;padding:0}
html,body{width:1200px;height:793px;overflow:hidden}
body{position:relative;background:var(--page);font-family:"Open Sans",Arial,sans-serif;color:var(--text)}

.site-header{position:absolute;left:0;top:0;width:1200px;height:45px;background:var(--brand);color:#fff}
.brand{position:absolute;left:26px;top:0;line-height:45px;font-size:14.5px;font-weight:600;letter-spacing:.1px}
.share{position:absolute;left:238px;top:0;width:228px;height:45px;background:var(--brand-dark);display:flex;align-items:center;gap:10px;padding-left:22px;font-size:11.5px;font-weight:400}
.level{position:absolute;left:796px;top:14px;width:178px}
.level-track{position:relative;height:4px;border-radius:2px;background:#fff}
.level-fill{position:absolute;left:0;top:0;width:93px;height:4px;border-radius:2px;background:var(--track-dark)}
.level-knob{position:absolute;left:87px;top:-4px;width:12px;height:12px;border-radius:50%;background:#fff}
.level-text{margin-top:8px;font-size:11px;font-weight:600}
.user-nav{position:absolute;left:1001px;top:8px;display:flex;align-items:center;font-size:11.5px;font-weight:400;height:28px}
.user-avatar{width:28px;height:28px;border-radius:50%;background:var(--avatar-user);margin-right:11px}
.user-nav .sep{margin:0 8px}
.user-nav .logout{display:flex;align-items:center;gap:5px}

.card{position:absolute;background:var(--card);border:1px solid var(--line);border-radius:2px}
.profile-card{left:26px;top:69px;width:458px;height:213px}
.profile-photo{position:absolute;left:28px;top:30px;width:66px;height:66px;border-radius:50%;background:linear-gradient(160deg,#2bb3a5,var(--avatar))}
.profile-info{position:absolute;left:126px;top:36px}
.profile-name{font-size:17px;line-height:20px;font-weight:400}
.profile-meta{font-size:10.7px;line-height:16px;color:#444;margin-bottom:8px}

.rating-label{font-size:11.5px;line-height:18px;color:#555}
.stars{display:flex;gap:2.5px;height:18.4px;align-items:center}
.stars svg{width:10px;height:10px}
.on{fill:var(--star-on)}
.off{fill:var(--star-off)}

.review-card{left:26px;top:300px;width:458px;height:362px;padding:24px 0 0 21px}
.review-title{font-size:12px;line-height:18px;font-weight:400;margin-bottom:3px}
.review-text{display:block;margin:12px 0 0 3px;width:406px;height:116px;border:1px solid var(--line);resize:vertical}
.skip{display:block;margin:10px 0 0 4px;width:89px;height:34px;border:0;border-radius:2px;background:var(--brand);color:#fff;font-family:inherit;font-size:11.5px}

.history-card{left:500px;top:69px;width:675px;height:593px}
.history-entry{margin:0 19px;padding:38px 0 25px 34px;border-bottom:1px solid var(--line)}
.history-entry + .history-entry{padding-top:42px}
.history-entry:last-child{border-bottom:0}
.entry-head{display:flex;align-items:center;height:22px;margin-bottom:8px}
.entry-title{font-family:Roboto,Arial,sans-serif;font-size:17px;color:#333}
.entry-date{display:flex;align-items:center;gap:10px;margin-left:14px;font-size:11.5px;color:var(--date)}
.entry-count{font-size:11.5px;line-height:20px;color:var(--muted)}
.entry-row{display:flex;align-items:center;gap:10px;font-size:11.5px;line-height:19.6px}

.site-footer{position:absolute;left:0;top:745px;width:1200px;height:48px;background:var(--brand);color:#fff;font-size:12.5px;display:flex;align-items:center;justify-content:center}
</style>
</head>
<body>
<svg width="0" height="0" style="position:absolute">
  <defs>
    <symbol id="star" viewBox="0 0 24 24"><path d="M12 1.5l3.2 7 7.6.8-5.7 5.1 1.6 7.5L12 18l-6.7 3.9 1.6-7.5L1.2 9.3l7.6-.8z"/></symbol>
    <symbol id="calendar" viewBox="0 0 16 16"><path fill="#a8a8a8" d="M2 3h12v12H2zM4 1h2v3H4zM10 1h2v3h-2z"/><path fill="#fff" d="M3 6h10v8H3z"/><path fill="#a8a8a8" d="M4 7h2v2H4zM7 7h2v2H7zM10 7h2v2h-2zM4 10h2v2H4zM7 10h2v2H7zM10 10h2v2h-2z"/></symbol>
  </defs>
</svg>

<header class="site-header">
  <div class="brand">TBD COMPANY NAME</div>
  <div class="share">
    <svg width="12" height="13" viewBox="0 0 12 13"><circle cx="9.5" cy="2.5" r="2.2" fill="#fff"/><circle cx="2.5" cy="6.5" r="2.2" fill="#fff"/><circle cx="9.5" cy="10.5" r="2.2" fill="#fff"/><path d="M9.5 2.5L2.5 6.5 9.5 10.5" stroke="#fff" stroke-width="1.3" fill="none"/></svg>
    Share this to get more points !
  </div>
  <div class="level">
    <div class="level-track"><div class="level-fill"></div><div class="level-knob"></div></div>
    <div class="level-text">Level 3-41 points to level 4</div>
  </div>
  <nav class="user-nav">
    <div class="user-avatar" role="img" aria-label="Your profile picture"></div>
    <span>Your Profile</span><span class="sep">|</span>
    <span class="logout"><svg width="10" height="12" viewBox="0 0 10 12"><path d="M2.5 5V3.5a2.5 2.5 0 015 0V5" stroke="#fff" stroke-width="1.5" fill="none"/><rect x="0.5" y="5" width="9" height="7" rx="1" fill="#fff"/></svg>Logout</span>
  </nav>
</header>

<section class="card profile-card">
  <div class="profile-photo" role="img" aria-label="Portrait of Sam Rivers"></div>
  <div class="profile-info">
    <h1 class="profile-name">Sam Rivers</h1>
    <p class="profile-meta">( Level 9 in product management ) ( Reviews : 5 | Score : 4 )</p>
    <div class="rating-label">smart</div>
    <div class="stars"><svg class="on"><use href="#star"/></svg><svg class="on"><use href="#star"/></svg><svg class="on"><use href="#star"/></svg><svg class="on"><use href="#star"/></svg><svg class="off"><use href="#star"/></svg></div>
    <div class="rating-label">Average Personality</div>
    <div class="stars"><svg class="on"><use href="#star"/></svg><svg class="on"><use href="#star"/></svg><svg class="on"><use href="#star"/></svg><svg class="off"><use href="#star"/></svg><svg class="off"><use href="#star"/></svg></div>
    <div class="rating-label">Works crazy hard</div>
    <div class="stars"><svg class="on"><use href="#star"/></svg><svg class="on"><use href="#star"/></svg><svg class="on"><use href="#star"/></svg><svg class="on"><use href="#star"/></svg><svg class="on"><use href="#star"/></svg></div>
  </div>
</section>

<section class="card review-card">
  <h2 class="review-title">Update your review fot this person</h2>
  <div class="rating-label">smart</div>
  <div class="stars"><svg class="on"><use href="#star"/></svg><svg class="on"><use href="#star"/></svg><svg class="on"><use href="#star"/></svg><svg class="on"><use href="#star"/></svg><svg class="off"><use href="#star"/></svg></div>
  <div class="rating-label">Average Personality</div>
  <div class="stars"><svg class="on"><use href="#star"/></svg><svg class="on"><use href="#star"/></svg><svg class="on"><use href="#star"/></svg><svg class="off"><use href="#star"/></svg><svg class="off"><use href="#star"/></svg></div>
  <div class="rating-label">Works crazy hard</div>
  <div class="stars"><svg class="on"><use href="#star"/></svg><svg class="on"><use href="#star"/></svg><svg class="on"><use href="#star"/></svg><svg class="on"><use href="#star"/></svg><svg class="on"><use href="#star"/></svg></div>
  <textarea class="review-text" aria-label="Your review"></textarea>
  <button class="skip" type="button">Skip</button>
</section>

<section class="card history-card">
  <article class="history-entry">
    <div class="entry-head"><span class="entry-title">Given By Coworker</span><span class="entry-date"><svg width="15" height="15"><use href="#calendar"/></svg>2016 - 25- 23</span></div>
    <div class="entry-count">Number of reviews :</div>
    <div class="entry-row">Smarts <span class="stars"><svg class="on"><use href="#star"/></svg><svg class="on"><use href="#star"/></svg><svg class="on"><use href="#star"/></svg><svg class="off"><use href="#star"/></svg><svg class="off"><use href="#star"/></svg></span></div>
    <div class="entry-row">Easy to work with <span class="stars"><svg class="on"><use href="#star"/></svg><svg class="on"><use href="#star"/></svg><svg class="on"><use href="#star"/></svg><svg class="off"><use href="#star"/></svg><svg class="off"><use href="#star"/></svg></span></div>
    <div class="entry-row">Hard worker <span class="stars"><svg class="on"><use href="#star"/></svg><svg class="on"><use href="#star"/></svg><svg class="on"><use href="#star"/></svg><svg class="off"><use href="#star"/></svg><svg class="off"><use href="#star"/></svg></span></div>
  </article>
  <article class="history-entry">
    <div class="entry-head"><span class="entry-title">Given By Coworker</span><span class="entry-date"><svg width="15" height="15"><use href="#calendar"/></svg>2016 - 25- 23</span></div>
    <div class="entry-count">Number of reviews :</div>
    <div class="entry-row">Smarts <span class="stars"><svg class="on"><use href="#star"/></svg><svg class="on"><use href="#star"/></svg><svg class="on"><use href="#star"/></svg><svg class="off"><use href="#star"/></svg><svg class="off"><use href="#star"/></svg></span></div>
    <div class="entry-row">Easy to work with <span class="stars"><svg class="on"><use href="#star"/></svg><svg class="on"><use href="#star"/></svg><svg class="on"><use href="#star"/></svg><svg class="off"><use href="#star"/></svg><svg class="off"><use href="#star"/></svg></span></div>
    <div class="entry-row">Hard worker <span class="stars"><svg class="on"><use href="#star"/></svg><svg class="on"><use href="#star"/></svg><svg class="on"><use href="#star"/></svg><svg class="off"><use href="#star"/></svg><svg class="off"><use href="#star"/></svg></span></div>
  </article>
  <article class="history-entry">
    <div class="entry-head"><span class="entry-title">Given By Coworker</span><span class="entry-date"><svg width="15" height="15"><use href="#calendar"/></svg>2016 - 25- 23</span></div>
    <div class="entry-count">Number of reviews :</div>
    <div class="entry-row">Smarts <span class="stars"><svg class="on"><use href="#star"/></svg><svg class="on"><use href="#star"/></svg><svg class="off"><use href="#star"/></svg><svg class="off"><use href="#star"/></svg><svg class="off"><use href="#star"/></svg></span></div>
    <div class="entry-row">Easy to work with <span class="stars"><svg class="on"><use href="#star"/></svg><svg class="on"><use href="#star"/></svg><svg class="on"><use href="#star"/></svg><svg class="off"><use href="#star"/></svg><svg class="off"><use href="#star"/></svg></span></div>
    <div class="entry-row">Hard worker <span class="stars"><svg class="on"><use href="#star"/></svg><svg class="on"><use href="#star"/></svg><svg class="on"><use href="#star"/></svg><svg class="off"><use href="#star"/></svg><svg class="off"><use href="#star"/></svg></span></div>
  </article>
</section>

<footer class="site-footer">Copyright 2016 | All Right Reserved</footer>
</body>
</html>
```